Innovative Consulting Firm Needs New Business Cards and Stationary

Our Innovative Consulting Firm, Larkfield Consulting, is in need of new business cards and stationary designs. We want two-sided cards that incorporate our logo, which is attached. We are looking for something not too formal, but is professional and slick.

Card should have the following information:
Name (ex. Tom Bradley)
Title (ex. Manager)
Address (ex. 24680 Cedar Lane)
Address 2 (ex. Suite 100)
City
State
Zip Code
Mobile
Email

The card should also have our website: www.larkfieldconsulting.example

Industry/Entity Type

Management Consulting

Contact Information for Business Card

Name (ex. Tom Bradley)
Title (ex. Manager)
Address 2 (ex. Suite 100)
City
State
Zip Code
Mobile
Email

Font styles to use
Sans Serif

Requirements
Must have
• The colors on the card must match the colors in the logo. The exact color codes are attached in a pdf.
Nice to have
• The Company's Tagline is "Focused on your Future". This might be nice to incorporate, but not necessary.

```html
<!DOCTYPE html>
<html lang="en">
<head>
<meta charset="utf-8">
<title>Larkfield Consulting – Business Cards</title>
<link rel="stylesheet" href="https://fonts.googleapis.com/css2?family=Source+Sans+3:wght@400;600;700&display=swap">
<style>
  :root {
    --brand-blue: #22609b;
    --brand-yellow: #f2c21b;
    --card-white: #f6f6f6;
    --page-bg: #e4e4e2;
    --text-white: #ffffff;
    --divider: rgba(255,255,255,0.55);
  }
  * { box-sizing: border-box; margin: 0; padding: 0; }
  html, body {
    width: 1200px; height: 780px; overflow: hidden;
    background: var(--page-bg);
    font-family: "Source Sans 3", Arial, sans-serif;
  }
  .sheet {
    width: 1200px; height: 780px;
    display: flex; align-items: center; justify-content: center; gap: 44px;
  }
  .card {
    width: 540px; height: 310px;
    background: var(--card-white);
    position: relative; overflow: hidden;
    box-shadow: 0 2px 8px rgba(0,0,0,0.12);
    display: flex; flex-direction: column;
  }

  /* Wordmark stand-in */
  .brand {
    display: flex; align-items: center; gap: 10px;
    color: var(--brand-blue);
    font-weight: 600;
    letter-spacing: 0.5px;
  }
  .brand-dot {
    width: 12px; height: 12px; border-radius: 50%;
    background: var(--brand-yellow); flex: none;
  }

  /* Front */
  .front-logo-area {
    height: 132px; display: flex; align-items: center; justify-content: center;
  }
  .front-logo-area .brand { font-size: 38px; }
  .name-band {
    height: 38px; background: var(--brand-yellow);
    display: flex; align-items: center; justify-content: center; gap: 8px;
    color: var(--text-white);
  }
  .name-band .person-name { font-size: 21px; font-weight: 700; }
  .name-band .sep { width: 1px; height: 18px; background: var(--text-white); }
  .name-band .person-title { font-size: 15px; font-weight: 400; }
  .contact-band {
    flex: 1; background: var(--brand-blue); color: var(--text-white);
    display: flex; flex-direction: column; justify-content: space-between;
    padding: 14px 0 10px;
  }
  .contact-columns {
    display: flex; justify-content: center; align-items: stretch; gap: 22px;
  }
  .contact-column { font-size: 14px; line-height: 1.3; text-align: right; }
  .contact-column.right { text-align: left; }
  .contact-line { display: flex; align-items: center; gap: 6px; }
  .contact-column .contact-line { justify-content: flex-end; }
  .contact-column.right .contact-line { justify-content: flex-start; }
  .contact-divider { width: 1px; background: var(--divider); }
  .icon-chip {
    width: 15px; height: 15px; background: var(--brand-yellow);
    display: inline-flex; align-items: center; justify-content: center; flex: none;
  }
  .website { text-align: center; font-size: 14px; letter-spacing: 0.2px; }
  .bottom-strip { height: 22px; background: var(--card-white); }

  /* Back */
  .back-logo-area {
    flex: 1; display: flex; align-items: center; justify-content: center;
  }
  .back-logo-area .brand { font-size: 40px; }
  .back-band {
    height: 46px; background: var(--brand-blue); color: var(--text-white);
    display: flex; align-items: center; justify-content: center;
    font-size: 15px; letter-spacing: 0.3px;
  }
</style>
</head>
<body>
<main class="sheet">

  <section class="card card-front" aria-label="Business card front">
    <div class="front-logo-area">
      <div class="brand"><span class="brand-dot"></span>Larkfield Consulting</div>
    </div>
    <div class="name-band">
      <span class="person-name">Tom Bradley</span>
      <span class="sep"></span>
      <span class="person-title">Manager</span>
    </div>
    <div class="contact-band">
      <div class="contact-columns">
        <div class="contact-column left">
          <div class="contact-line">tom.bradley@larkfield.example
            <span class="icon-chip">
              <svg width="11" height="9" viewBox="0 0 11 9"><rect x="0.5" y="0.5" width="10" height="8" fill="none" stroke="#22609b"/><path d="M0.5 0.5 L5.5 5 L10.5 0.5" fill="none" stroke="#22609b"/></svg>
            </span>
          </div>
          <div>24680 Cedar Lane</div>
          <div>Suite 100, USA</div>
        </div>
        <div class="contact-divider"></div>
        <div class="contact-column right">
          <div class="contact-line">
            <span class="icon-chip">
              <svg width="11" height="11" viewBox="0 0 11 11"><path d="M2 1 L4 1 L4.8 3.3 L3.6 4.3 C4.2 5.6 5.3 6.7 6.6 7.3 L7.6 6.1 L10 6.9 L10 9 C10 9.6 9.5 10 9 10 C4.6 10 1 6.4 1 2 C1 1.4 1.4 1 2 1 Z" fill="#22609b"/></svg>
            </span>+61 555 010 246
          </div>
          <div>24680 Cedar Lane</div>
          <div>Suite 100, USA</div>
        </div>
      </div>
      <div class="website">www.larkfieldconsulting.example</div>
    </div>
    <div class="bottom-strip"></div>
  </section>

  <section class="card card-back" aria-label="Business card back">
    <div class="back-logo-area">
      <div class="brand"><span class="brand-dot"></span>Larkfield Consulting</div>
    </div>
    <div class="back-band">www.larkfieldconsulting.example</div>
  </section>

</main>
</body>
</html>
```